Wordpress Layout, Plug-in, Mash-up Overhaul

We have collection of vertical topic portals; in each portal, a post typically is an article which goes with a subject video, following are 5 reference sites:

http://www.tallymint.com/
http://www.ladycounsel.com/
http://www.sparkvista.tv/
http://www.dwellingview.com/
http://www.gallerhum.com/

We obtained most of our based WP theme from various premium WP template membership sites, subsequently re-organise, mash-up content to produce sites as above; however we start to be constraint as we get into a fixed pattern of laying out our contents and we seeking professional help to re-work this. these re-work can includes as follows.

1. proposal on creative re-placement of component / re-layout on the templates. Should also suggest different way for the advertising banner placement etc.

2. proposal on right and appropriate use of WP plugins (paid or free but have to be secured and reliable) to achieve more relevant add-on of content where necessary (rss, etc)

Objective:
We want to move away from our internal team design constraint and also moving alway from being stuck with certain stereo-type way of WP content site. However the proposed WP design should still be a portal-centric type vs blogging/product-centric.

Deliverables:
1. We don't need the actual cut template but a design mockup of the home page and relevant sub pages (.psd, jpg etc) for the proposed re-design. Based on the above 5 listed sites, the deliverable would be at least 10 pages of design layout work (considering home page and 1 sub pages for each domain; could be more if necessary)

2. The plugins reference where necessary

What's expected from your proposal for the bid:
We would like a mockup of a re-design from any pick from any of the above 5 domains

```html
<!DOCTYPE html>
<html lang="en">
<head>
<meta charset="utf-8">
<title>Tallymint — Home</title>
<link href="https://fonts.googleapis.com/css2?family=Arimo:wght@400;700&family=Roboto+Condensed:wght@400;700&family=Roboto:wght@300;400&display=swap" rel="stylesheet">
<style>
:root{
  --navy:#2a5878;
  --navy-dark:#224a66;
  --ink:#333;
  --muted:#6f6f6f;
  --rule:#dcdcdc;
  --paper:#fff;
  --tab-off:#e2e2e2;
  --footer:#3b3b3b;
  --footer-base:#2c2c2c;
  --footer-text:#bdbdbd;
}
*{box-sizing:border-box;margin:0;padding:0}
html,body{width:1200px;height:3152px;overflow:hidden}
body{font-family:"Arimo",Arial,sans-serif;color:var(--ink);background:var(--paper)}
.page{position:relative;width:1200px;height:3152px;overflow:hidden}
.abs{position:absolute}
.photo{position:absolute}
a{color:inherit;text-decoration:none}

/* header */
.brand{left:172px;top:16px;display:flex;align-items:center;gap:12px}
.brand-mark{width:44px;height:44px;background:var(--navy)}
.brand-name{font-family:"Arimo",sans-serif;font-weight:700;font-size:30px;color:var(--navy)}
.top-links{top:30px;font-size:13px;color:#555}
.main-nav{left:0;top:74px;width:1200px;height:40px;background:var(--navy)}
.main-nav span{position:absolute;top:12px;font-size:13px;color:#fff;transform:translateX(-50%);white-space:nowrap}

/* hero */
.hero{left:0;top:114px;width:1200px;height:416px;background:linear-gradient(90deg,#d9d6d2 0%,#f4f3f1 35%,#eef0f2 60%,#d8dce0 100%)}
.hero-title{left:666px;top:206px;font-family:"Roboto",sans-serif;font-weight:300;font-size:46px;color:var(--navy)}
.hero-sub{left:666px;top:266px;font-family:"Roboto",sans-serif;font-size:22px;color:#222}
.hero-text{left:666px;top:306px;width:320px;font-size:12.5px;line-height:20px;color:#333}
.btn{display:flex;align-items:center;justify-content:center;background:var(--navy);color:#fff;font-size:14px}
.hero-btn{left:666px;top:389px;width:214px;height:44px}

/* headings */
.section-title{font-family:"Roboto Condensed",sans-serif;font-weight:700;font-size:19px;color:var(--navy);text-transform:uppercase}

/* posts */
.post-date{font-family:"Roboto Condensed",sans-serif;color:var(--navy);font-size:13px;line-height:19px}
.post-date b{display:block;font-size:15px;font-weight:400}
.date-rule{width:1px;height:50px;background:#bbb}
.post-title{font-family:"Roboto Condensed",sans-serif;font-size:19px;color:var(--navy);text-transform:uppercase}
.rule{height:1px;background:var(--rule)}
.excerpt{font-size:11.5px;line-height:18px;color:#444}
.share{display:flex;gap:4px}
.share i{display:block;width:38px;height:38px}
.comments{display:flex;align-items:center;gap:8px;font-size:11px;color:#777}

/* pagination */
.pager{display:flex;gap:7px}
.pager span{height:26px;min-width:26px;padding:0 8px;border:1px solid #ccc;font-size:12px;display:flex;align-items:center;justify-content:center;color:#333;background:#fafafa}

/* grid cards */
.card-title{font-size:12px;color:var(--navy)}
.card-sub{font-size:11px;color:#444}

/* sidebar */
.search{left:721px;top:567px;width:307px;height:36px;border:1px solid #ccc;font-size:11px;color:#666;padding:10px 16px}
.welcome-title{font-family:"Roboto Condensed",sans-serif;font-weight:700;font-size:17px;color:var(--navy)}
.welcome-text{font-size:11px;line-height:20px;color:#555}
.cat-list{left:721px;top:1274px;width:246px;list-style:none}
.cat-list li{height:33px;border-bottom:1px solid #e3e3e3;font-size:11px;color:#555;display:flex;align-items:center;gap:10px;padding-left:4px}
.cat-list li::before{content:"";width:5px;height:5px;border-top:1px solid #999;border-right:1px solid #999;transform:rotate(45deg)}
.tabs{left:721px;top:1526px;width:307px;height:32px;display:flex;font-size:12px}
.tabs span{flex:1;display:flex;align-items:center;justify-content:center}
.tab-on{background:var(--navy);color:#fff}
.tab-off{background:var(--tab-off);color:#555}
.mini{position:absolute;left:721px;width:307px;height:97px;border-bottom:1px solid #e3e3e3}
.mini .thumb{position:absolute;left:0;top:6px;width:84px;height:84px}
.mini h4{position:absolute;left:107px;top:12px;font-weight:400;font-size:12px;color:var(--navy)}
.mini p{position:absolute;left:107px;top:34px;width:200px;font-size:10.5px;line-height:20px;color:#555}
.recent-item{position:absolute;left:721px;width:307px}
.recent-item .thumb{position:absolute;left:0;top:0;width:130px;height:94px}
.recent-item h4{position:absolute;left:150px;top:4px;font-weight:400;font-size:12px;color:var(--navy)}
.recent-item p{position:absolute;left:150px;top:26px;width:150px;font-size:10.5px;line-height:21px;color:#555}

/* footer */
.footer{left:0;top:2888px;width:1200px;height:214px;background:var(--footer)}
.footer-base{left:0;top:3102px;width:1200px;height:50px;background:var(--footer-base)}
.foot-col{list-style:none;font-size:10px;color:var(--footer-text)}
.foot-col li{height:22px}
.foot-heading{font-size:15px;color:#fff}
.foot-social{display:flex;align-items:center;gap:10px;font-size:10px;color:var(--footer-text)}
.foot-social i{width:28px;height:28px;border-radius:50%;background:#5a5a5a;display:block}
.copyright{left:0;top:3121px;width:1200px;text-align:center;font-size:10px;color:#999}
</style>
</head>
<body>
<div class="page">

  <!-- header -->
  <div class="abs brand"><span class="brand-mark"></span><span class="brand-name">Tallymint</span></div>
  <span class="abs top-links" style="left:500px">About Us</span>
  <span class="abs top-links" style="left:601px">Advertise With Us</span>
  <span class="abs top-links" style="left:746px">Contact Us</span>
  <span class="abs top-links" style="left:855px">Privacy Policy</span>
  <span class="abs top-links" style="left:977px">Sitemap</span>

  <nav class="abs main-nav">
    <span style="left:212px">Home</span>
    <span style="left:343px">Financial Management</span>
    <span style="left:483px">Insurance</span>
    <span style="left:586px">Investing</span>
    <span style="left:681px">Loans</span>
    <span style="left:782px">Real Estate</span>
    <span style="left:897px">Retirement</span>
    <span style="left:988px">Tax</span>
  </nav>

  <!-- hero -->
  <div class="abs hero" role="img" aria-label="Smiling businesswoman in glasses in a bright office, colleagues blurred behind"></div>
  <svg class="abs" style="left:74px;top:280px" width="24" height="70" viewBox="0 0 24 70"><polyline points="22,2 2,35 22,68" fill="none" stroke="#fff" stroke-width="2"/></svg>
  <svg class="abs" style="left:1120px;top:280px" width="24" height="70" viewBox="0 0 24 70"><polyline points="2,2 22,35 2,68" fill="none" stroke="#fff" stroke-width="2"/></svg>
  <h1 class="abs hero-title">Tallymint</h1>
  <p class="abs hero-sub">Many desktop publishing packages</p>
  <p class="abs hero-text">Many desktop publishing packages and web page editors now use Lorem Ipsum as their default model text, and a search for 'lorem ipsum' will uncover...</p>
  <a class="abs btn hero-btn">Click here for more info</a>

  <!-- video -->
  <div class="photo" style="left:172px;top:567px;width:519px;height:315px;background:linear-gradient(135deg,#9aa0a6,#e4e5e6 55%,#c9ccce)" role="img" aria-label="Video still of a woman working with papers and a tablet at a desk"></div>
  <svg class="abs" style="left:390px;top:690px" width="84" height="70" viewBox="0 0 84 70"><rect width="84" height="70" rx="8" fill="#2e2e2e" opacity=".8"/><polygon points="32,18 58,35 32,52" fill="#4aa3df"/></svg>
  <div class="abs" style="left:172px;top:882px;width:519px;height:32px;background:#1f1f1f"></div>
  <svg class="abs" style="left:172px;top:882px" width="519" height="32" viewBox="0 0 519 32"><rect x="6" y="5" width="36" height="22" fill="#3a3a3a"/><polygon points="19,10 29,16 19,22" fill="#fff"/><rect x="54" y="14" width="390" height="4" fill="#555"/><rect x="54" y="14" width="60" height="4" fill="#4aa3df"/></svg>

  <!-- recent posts -->
  <h2 class="abs section-title" style="left:172px;top:943px">Recent Posts</h2>

  <div class="photo" style="left:172px;top:990px;width:519px;height:391px;background:linear-gradient(135deg,#d8d8d8,#6d6d6d 55%,#2a2a2a)" role="img" aria-label="Black and white close-up of a businessman's wristwatch and suit sleeve"></div>
  <div class="abs post-date" style="left:174px;top:1410px">MARCH<b>20-2014</b></div>
  <div class="abs date-rule" style="left:252px;top:1406px"></div>
  <h3 class="abs post-title" style="left:280px;top:1420px">How to prepare a personal budget</h3>
  <div class="abs rule" style="left:172px;top:1482px;width:519px"></div>
  <p class="abs excerpt" style="left:172px;top:1493px;width:519px">Many desktop publishing packages and web page editors now use Lorem Ipsum as their default model text, and a search for 'lorem ipsum' will uncover...</p>
  <div class="abs share" style="left:172px;top:1549px"><i style="background:#2aa3dc"></i><i style="background:#3b5998"></i><i style="background:#c4302b"></i><i style="background:#4e7ea2"></i><i style="background:#cb2027"></i><i style="background:#dc4a38"></i></div>
  <div class="abs comments" style="left:566px;top:1552px"><svg width="34" height="34" viewBox="0 0 34 34"><circle cx="17" cy="17" r="16" fill="#fff" stroke="#ccc"/><path d="M9 12h16v9h-9l-4 4v-4h-3z" fill="#aaa"/></svg>102 Comments</div>

  <div class="photo" style="left:172px;top:1631px;width:519px;height:393px;background:linear-gradient(135deg,#f2f2f0,#dfe3e8 50%,#6b8fc2)" role="img" aria-label="Smiling woman in a blue shirt using a laptop on a white sofa"></div>
  <div class="abs post-date" style="left:174px;top:2052px">MARCH<b>20-2014</b></div>
  <div class="abs date-rule" style="left:252px;top:2048px"></div>
  <h3 class="abs post-title" style="left:280px;top:2063px">How to prepare a personal budget</h3>
  <div class="abs rule" style="left:172px;top:2123px;width:519px"></div>
  <p class="abs excerpt" style="left:172px;top:2135px;width:519px">Many desktop publishing packages and web page editors now use Lorem Ipsum as their default model text, and a search for 'lorem ipsum' will uncover...</p>
  <div class="abs share" style="left:172px;top:2194px"><i style="background:#2aa3dc"></i><i style="background:#3b5998"></i><i style="background:#c4302b"></i><i style="background:#4e7ea2"></i><i style="background:#cb2027"></i><i style="background:#dc4a38"></i></div>
  <div class="abs comments" style="left:566px;top:2196px"><svg width="34" height="34" viewBox="0 0 34 34"><circle cx="17" cy="17" r="16" fill="#fff" stroke="#ccc"/><path d="M9 12h16v9h-9l-4 4v-4h-3z" fill="#aaa"/></svg>102 Comments</div>

  <div class="abs pager" style="left:307px;top:2269px"><span>Prev</span><span>1</span><span>2</span><span>3</span><span>4</span><span>5</span><span>6</span><span>...</span><span>22</span><span>Next</span></div>

  <!-- financial management -->
  <h2 class="abs section-title" style="left:172px;top:2328px">Financial Management</h2>
  <div class="photo" style="left:172px;top:2377px;width:246px;height:130px;background:linear-gradient(135deg,#c9d2dc,#8fa3b8)" role="img" aria-label="Adviser meeting a couple at a desk"></div>
  <div class="photo" style="left:443px;top:2377px;width:246px;height:130px;background:linear-gradient(135deg,#e6ecf0,#a9b9c6)" role="img" aria-label="Two business people shaking hands in a glass office"></div>
  <p class="abs card-title" style="left:172px;top:2519px">How To Prepare A Personal Budget</p>
  <p class="abs card-sub" style="left:172px;top:2543px">Whether you are looking to save up for a...</p>
  <p class="abs card-title" style="left:443px;top:2519px">How To Prepare A Personal Budget</p>
  <p class="abs card-sub" style="left:443px;top:2543px">Whether you are looking to save up for a...</p>
  <div class="photo" style="left:172px;top:2583px;width:246px;height:130px;background:linear-gradient(135deg,#f0e4dc,#c9a58c)" role="img" aria-label="Hands with a pen over a printed bar chart"></div>
  <div class="photo" style="left:443px;top:2583px;width:246px;height:130px;background:linear-gradient(135deg,#e2e2e2,#8a8a8a)" role="img" aria-label="Group of hands joined together over a table"></div>
  <p class="abs card-title" style="left:172px;top:2725px">How To Prepare A Personal Budget</p>
  <p class="abs card-sub" style="left:172px;top:2749px">Whether you are looking to save up for a...</p>
  <p class="abs card-title" style="left:443px;top:2725px">How To Prepare A Personal Budget</p>
  <p class="abs card-sub" style="left:443px;top:2749px">Whether you are looking to save up for a...</p>
  <a class="abs btn" style="left:506px;top:2797px;width:185px;height:40px;font-size:12px">View more recent Posts</a>

  <!-- sidebar -->
  <div class="abs search">Search :</div>
  <svg class="abs" style="left:998px;top:577px" width="16" height="16" viewBox="0 0 16 16"><circle cx="6.5" cy="6.5" r="5" fill="none" stroke="#bbb" stroke-width="1.6"/><line x1="10.5" y1="10.5" x2="15" y2="15" stroke="#bbb" stroke-width="1.6"/></svg>
  <div class="photo" style="left:721px;top:620px;width:307px;height:168px;background:linear-gradient(135deg,#d7dade,#8c949c 60%,#c5c9cd)" role="img" aria-label="Group of business people in suits standing together"></div>
  <h3 class="abs welcome-title" style="left:721px;top:810px">WELCOME TO NORA VALE</h3>
  <p class="abs welcome-text" style="left:721px;top:834px;width:307px">We are a news source for all things related to business and finance. Our aim is to connect global events to their economic ramifications, giving you the news you need to make the right decisions. In a world of global instability, having news coverage that is fast, thorough, and in-depth is an invaluable asset...</p>

  <div class="photo" style="left:729px;top:970px;width:288px;height:241px;background:linear-gradient(160deg,#ffffff 0%,#f3d9a8 45%,#e58a1f 100%);border:1px solid #333" role="img" aria-label="Banner advertisement for a streaming privacy service"></div>

  <h3 class="abs welcome-title" style="left:721px;top:1238px;font-size:15px">CATEGORIES</h3>
  <ul class="abs cat-list">
    <li>Financial Management</li><li>Insurance</li><li>Investing</li><li>Loans</li><li>Real Estate</li><li>Retirement</li><li>Tax</li>
  </ul>

  <div class="abs tabs"><span class="tab-on">Popular Posts</span><span class="tab-off">Recent Posts</span></div>

  <div class="mini" style="top:1574px"><div class="thumb" style="background:linear-gradient(135deg,#e9dcd2,#9a7c6a)" role="img" aria-label="Business team photo"></div><h4>Repaying A Loan</h4><p>We are a news source for all things related to business and finance...</p></div>
  <div class="mini" style="top:1671px"><div class="thumb" style="background:linear-gradient(135deg,#dfe7ea,#7e9aa4)" role="img" aria-label="Businessman jumping"></div><h4>Repaying A Loan</h4><p>We are a news source for all things related to business and finance...</p></div>
  <div class="mini" style="top:1768px"><div class="thumb" style="background:linear-gradient(135deg,#f1e6e0,#b79a8c)" role="img" aria-label="Hands holding a document"></div><h4>Repaying A Loan</h4><p>We are a news source for all things related to business and finance...</p></div>
  <div class="mini" style="top:1865px"><div class="thumb" style="background:linear-gradient(135deg,#e4e7ea,#8a9097)" role="img" aria-label="Man relaxing with a laptop"></div><h4>Repaying A Loan</h4><p>We are a news source for all things related to business and finance...</p></div>
  <div class="mini" style="top:1962px"><div class="thumb" style="background:linear-gradient(135deg,#efe6da,#b8a081)" role="img" aria-label="Woman in glasses portrait"></div><h4>Repaying A Loan</h4><p>We are a news source for all things related to business and finance...</p></div>
  <div class="mini" style="top:2059px"><div class="thumb" style="background:linear-gradient(135deg,#f2eeee,#c2b2b2)" role="img" aria-label="Hands on a calculator"></div><h4>Repaying A Loan</h4><p>We are a news source for all things related to business and finance...</p></div>

  <div class="photo" style="left:729px;top:2179px;width:288px;height:240px;background:linear-gradient(180deg,#2e6fc0 0%,#e9a33a 40%,#d9482a 100%);border:1px solid #333" role="img" aria-label="Banner advertisement for paid work from home"></div>

  <h3 class="abs welcome-title" style="left:721px;top:2447px;font-size:15px">RECENT</h3>
  <div class="recent-item" style="top:2484px"><div class="thumb" style="background:linear-gradient(135deg,#eef0f2,#9aa3ad)" role="img" aria-label="Woman working at a laptop"></div><h4>Repaying A Loan</h4><p>We are a news source for all things related to business and finance...</p></div>
  <div class="recent-item" style="top:2614px"><div class="thumb" style="background:linear-gradient(135deg,#f5f5f5,#8fcf6a)" role="img" aria-label="Green marker ticking a checkbox"></div><h4>Repaying A Loan</h4><p>We are a news source for all things related to business and finance...</p></div>
  <a class="abs btn" style="left:843px;top:2761px;width:185px;height:40px;font-size:12px">View more recent Posts</a>

  <!-- footer -->
  <footer class="abs footer"></footer>
  <ul class="abs foot-col" style="left:174px;top:2926px"><li>About Us</li><li>Advertise With Us</li><li>Contact Us</li><li>Privacy Policy</li><li>Sitemap</li></ul>
  <ul class="abs foot-col" style="left:330px;top:2926px"><li>Home</li><li>Financial Management</li><li>Insurance</li><li>Investing</li><li>Loans</li><li>Real Estate</li><li>Retirement</li><li>Tax</li></ul>
  <ul class="abs foot-col" style="left:509px;top:2926px"><li>Web development</li><li>App development</li><li>Video production</li><li>Content marketing</li><li>Social media</li></ul>
  <h4 class="abs foot-heading" style="left:675px;top:2922px;font-weight:400">Financial management</h4>
  <ul class="abs foot-col" style="left:675px;top:2960px"><li>How To Prepare A Personal Budget</li><li>How To Create A Balance Sheet</li><li>How To Manage Your Finances</li></ul>
  <ul class="abs foot-col" style="left:872px;top:2960px"><li>How To Protect Your Money</li><li>How To Do Financial Planning</li></ul>
  <div class="abs foot-social" style="left:675px;top:3036px"><i></i>Social Page</div>
  <div class="abs foot-social" style="left:795px;top:3036px"><i></i>Pin Board</div>
  <div class="abs foot-social" style="left:904px;top:3036px"><i></i>RSS</div>
  <div class="abs footer-base"></div>
  <p class="abs copyright">Copyright © 2014. Tallymint. All Rights Reserved</p>

</div>
</body>
</html>
```